Business Card Design Project

We are not a new company, but renamed to "Norvanta Kitchens" last year. We specialize in modern high-end cabinetry imports. We would like to communicate a sense of quality and cutting edge technology. Ideally the design would incorporate our logo colors, silver, red and preferably a black, matte background. Though we are open to suggestions.
Logo is attached.
Edit: I have attached rough drafts of the previous cards, this way you will have all necessary content that needs to go on the cards.
Reason: We have received a lot of great designs, but due to the sheer number we couldn't respond to all. We will extend the deadline for another 7 days to finalize and provide feedback to designers.
Thank you for your hard work!
Industry/Entity Type
Business
Look and feel
Each slider illustrates characteristics of the customer's brand and the style your logo design should communicate.

```html
<!DOCTYPE html>
<html lang="en">
<head>
<meta charset="utf-8">
<title>Norvanta Kitchens Business Card</title>
<link href="https://fonts.googleapis.com/css2?family=Michroma&display=swap" rel="stylesheet">
<style>
  :root {
    --page-bg: #d9d9d9;
    --card-black: #0d0d0d;
    --card-panel: #1a1a1a;
    --silver: #c9c9c9;
    --silver-light: #efefef;
    --brand-red: #e0242b;
    --text-white: #f2f2f2;
  }
  * { margin: 0; padding: 0; box-sizing: border-box; }
  html, body {
    width: 1200px; height: 861px; overflow: hidden;
    background: var(--page-bg);
    font-family: "Michroma", sans-serif;
  }
  .card-sheet {
    position: relative; width: 1200px; height: 861px;
    display: flex; justify-content: center; align-items: center; gap: 60px;
  }
  .card {
    position: relative; width: 510px; height: 292px;
    background: var(--card-black);
    overflow: hidden;
    box-shadow: 0 6px 18px rgba(0,0,0,0.25);
  }
  .card-texture {
    position: absolute; inset: 0;
    background: radial-gradient(ellipse at 60% 40%, #242424 0%, #0d0d0d 75%);
  }
  .card-sheen {
    position: absolute; top: -40px; bottom: -40px; left: 120px; width: 170px;
    background: linear-gradient(90deg, rgba(255,255,255,0) 0%, rgba(255,255,255,0.06) 50%, rgba(255,255,255,0) 100%);
    transform: skewX(-22deg);
  }
  /* Front */
  .brand-lockup {
    position: absolute; left: 0; right: 0; top: 50%;
    transform: translateY(-50%);
    display: flex; align-items: center; justify-content: center; gap: 14px;
  }
  .brand-square {
    width: 22px; height: 22px; background: var(--silver);
  }
  .brand-name {
    font-size: 24px; letter-spacing: 1px; color: var(--silver);
  }
  /* Back */
  .name-panel {
    position: absolute; top: 0; bottom: 0; left: -60px; width: 300px;
    background: var(--card-panel);
    transform: skewX(-22deg);
    border-right: 1px solid #2b2b2b;
  }
  .person {
    position: absolute; left: 36px; bottom: 70px;
  }
  .person-name {
    font-size: 17px; color: var(--brand-red); letter-spacing: 0.5px;
  }
  .person-title {
    margin-top: 4px; font-size: 12px; color: var(--text-white);
    padding-left: 70px;
  }
  .contact-list {
    position: absolute; left: 268px; top: 58px;
    list-style: none;
  }
  .contact-item {
    display: flex; align-items: flex-start; gap: 10px;
    font-size: 10px; line-height: 14px; color: var(--text-white);
    margin-bottom: 14px;
  }
  .contact-icon {
    flex: 0 0 18px; width: 18px; height: 18px;
    border-radius: 50%; background: var(--brand-red);
    display: flex; align-items: center; justify-content: center;
  }
  .contact-icon svg { width: 10px; height: 10px; fill: #111; }
</style>
</head>
<body>
<main class="card-sheet">
  <section class="card card-front" aria-label="Business card front">
    <div class="card-texture" role="img" aria-label="Dark carbon fibre texture"></div>
    <div class="card-sheen"></div>
    <div class="brand-lockup">
      <span class="brand-square"></span>
      <span class="brand-name">Norvanta Kitchens</span>
    </div>
  </section>

  <section class="card card-back" aria-label="Business card back">
    <div class="card-texture" role="img" aria-label="Dark carbon fibre texture"></div>
    <div class="name-panel"></div>
    <div class="person">
      <p class="person-name">MAREK HALDEN</p>
      <p class="person-title">President</p>
    </div>
    <ul class="contact-list">
      <li class="contact-item">
        <span class="contact-icon"><svg viewBox="0 0 10 10"><path d="M5 0.5a3.2 3.2 0 0 0-3.2 3.2C1.8 6.2 5 9.5 5 9.5s3.2-3.3 3.2-5.8A3.2 3.2 0 0 0 5 0.5zm0 4.5a1.3 1.3 0 1 1 0-2.6 1.3 1.3 0 0 1 0 2.6z"/></svg></span>
        <span>2158 - 84 St.<br>Riverford, AB T4K 2M9</span>
      </li>
      <li class="contact-item">
        <span class="contact-icon"><svg viewBox="0 0 10 10"><path d="M2.2 0.8l1.6 1.9-0.9 1.2c0.6 1.3 1.6 2.3 2.9 2.9l1.2-0.9 1.9 1.6-0.9 1.6C4.2 8.9 1.1 5.8 0.8 1.7z"/></svg></span>
        <span>555.210.0437</span>
      </li>
      <li class="contact-item">
        <span class="contact-icon"><svg viewBox="0 0 10 10"><path d="M2.5 0.8h5v2.4h-5zM1 3.8h8v4h-1.5v1.4h-5V7.8H1zM3.3 6.2v2h3.4v-2z"/></svg></span>
        <span>555.210.0482</span>
      </li>
      <li class="contact-item">
        <span class="contact-icon"><svg viewBox="0 0 10 10"><path d="M3 0.5h4a0.6 0.6 0 0 1 0.6 0.6v7.8a0.6 0.6 0 0 1-0.6 0.6H3a0.6 0.6 0 0 1-0.6-0.6V1.1A0.6 0.6 0 0 1 3 0.5zm0.4 1.2v5.6h3.2V1.7zM5 7.8a0.5 0.5 0 1 0 0 1 0.5 0.5 0 0 0 0-1z"/></svg></span>
        <span>555.318.2064</span>
      </li>
      <li class="contact-item">
        <span class="contact-icon"><svg viewBox="0 0 10 10"><path d="M0.8 2h8.4v6H0.8zm0.9 0.8L5 5.4l3.3-2.6z"/></svg></span>
        <span>dana@norvantakitchens.ca</span>
      </li>
    </ul>
  </section>
</main>
</body>
</html>
```